Harlow Terrain Consultants
Business Card and Stationary Design
Professional
Paul Dorrick, PE
4259 Copper Fern Lane
Alder Springs, Ohio 43817
paul@harlow-terrain.com

```html
<!DOCTYPE html>
<html lang="en">
<head>
<meta charset="utf-8">
<title>Harlow Terrain Consultants — Stationery</title>
<link rel="stylesheet" href="https://fonts.googleapis.com/css2?family=Cinzel:wght@500&family=Arimo:wght@400&display=swap">
<style>
  :root {
    --page: #ffffff;
    --frame: #d9d9d9;
    --paper: #ffffff;
    --blue-deep: #1f4f9c;
    --blue-mid: #3f78c8;
    --blue-soft: #9fbbe3;
    --brand: #3a6b3c;
    --ink-blue: #2f62b0;
    --ink-grey: #6a6a6a;
    --mark-tint: #e7ebf3;
    --mark-tint-2: #eef1e4;
  }
  * { box-sizing: border-box; margin: 0; padding: 0; }
  html, body { width: 1200px; height: 840px; overflow: hidden; background: var(--page); }
  .canvas { position: relative; width: 1200px; height: 840px; }
  .presentation-frame {
    position: absolute; left: 29px; top: 53px; width: 1142px; height: 729px;
    border: 1px solid var(--frame);
  }
  .sheet {
    position: absolute; background: var(--paper);
    box-shadow: 0 1px 4px rgba(0,0,0,0.18);
    overflow: hidden;
  }
  .band {
    position: absolute; left: 0; right: 0;
    background: linear-gradient(90deg, var(--blue-soft), var(--blue-mid) 35%, var(--blue-deep));
  }
  .wordmark {
    position: absolute; font-family: "Cinzel", serif; font-weight: 500;
    color: var(--brand); text-transform: uppercase; line-height: 1.2;
    display: flex; flex-direction: column; align-items: flex-start; gap: 6px;
  }
  .wordmark .dot { border-radius: 50%; background: var(--blue-mid); }
  .faint-mark {
    position: absolute; border-radius: 50%;
    background: radial-gradient(circle at 40% 40%, var(--mark-tint-2), var(--mark-tint) 70%);
  }
  .contact {
    position: absolute; font-family: "Arimo", sans-serif; font-style: normal;
    color: var(--ink-blue); line-height: 1.35; white-space: nowrap;
  }

  /* Letterhead */
  .letterhead { left: 523px; top: 72px; width: 523px; height: 682px; z-index: 1; }
  .letterhead .band.bottom { bottom: 22px; height: 12px; }
  .letterhead .wordmark { left: 16px; top: 36px; font-size: 13px; }
  .letterhead .wordmark .dot { width: 30px; height: 30px; margin-left: 20px; }
  .letterhead .contact { right: 34px; top: 14px; font-size: 8px; text-align: right; }
  .letterhead .faint-mark { left: 130px; top: 290px; width: 290px; height: 290px; }

  /* Envelope */
  .envelope { left: 65px; top: 341px; width: 564px; height: 252px; z-index: 2; }
  .envelope .flap { position: absolute; left: 0; top: 0; width: 564px; height: 16px; }
  .envelope .band.top { top: 14px; height: 8px; }
  .envelope .band.bottom { bottom: 0; height: 10px; }
  .envelope .wordmark { left: 8px; top: 34px; font-size: 13px; gap: 5px; }
  .envelope .wordmark .dot { width: 28px; height: 28px; margin-left: 50px; }
  .envelope .contact { left: 8px; top: 116px; font-size: 8px; }
  .envelope .faint-mark { left: 430px; top: 120px; width: 130px; height: 130px; }

  /* Business card */
  .business-card { left: 931px; top: 206px; width: 211px; height: 142px; z-index: 3; }
  .business-card .wordmark { left: 10px; top: 10px; font-size: 7px; gap: 3px; }
  .business-card .wordmark .dot { width: 12px; height: 12px; margin-left: 12px; }
  .business-card .person { position: absolute; left: 10px; top: 54px; font-family: "Arimo", sans-serif; font-size: 7px; color: var(--ink-grey); }
  .business-card .contact { left: 10px; top: 74px; font-size: 5.5px; }
  .business-card .faint-mark { left: 140px; top: 30px; width: 80px; height: 80px; }
</style>
</head>
<body>
<main class="canvas">
  <div class="presentation-frame"></div>

  <section class="sheet letterhead" aria-label="Letterhead">
    <div class="wordmark"><span class="dot"></span><span>Harlow Terrain<br>Consultants</span></div>
    <address class="contact">4259 Copper Fern Lane<br>Alder Springs, Ohio 43817<br>Phone: 614.555.0147</address>
    <div class="faint-mark" role="img" aria-label="Faint brand watermark"></div>
    <div class="band bottom"></div>
  </section>

  <section class="sheet envelope" aria-label="Envelope">
    <svg class="flap" viewBox="0 0 564 16" aria-hidden="true">
      <polyline points="0,15 10,1 554,1 564,15" fill="none" stroke="#cfd6e2" stroke-width="1"/>
    </svg>
    <div class="band top"></div>
    <div class="wordmark"><span class="dot"></span><span>Harlow Terrain<br>Consultants</span></div>
    <address class="contact">4259 Copper Fern Lane, Alder Springs, Ohio 43817</address>
    <div class="faint-mark" role="img" aria-label="Faint brand watermark"></div>
    <div class="band bottom"></div>
  </section>

  <section class="sheet business-card" aria-label="Business card">
    <div class="wordmark"><span class="dot"></span><span>Harlow Terrain<br>Consultants</span></div>
    <p class="person">Paul Dorrick, PE</p>
    <address class="contact">4259 Copper Fern Lane<br>Alder Springs, Ohio 43817<br>Office: 614.555.0147<br>Mobile: 614.555.0193<br>paul@harlow-terrain.com</address>
    <div class="faint-mark" role="img" aria-label="Faint brand watermark"></div>
  </section>
</main>
</body>
</html>
```